KTR Associates Business Card

I would like to have a business card designed that uses my current logo and colors. I am not looking for anything to "out there" but can have a little fun so that it stands out.

I have a boutique consulting firm that specializes in strategic planning, change management, leadership development and innovation.

Industry/Entity Type

Leadership

Contact Information for Business Card

Marta Holloway
President
marta@ktr-associates-mail.com
919-555-0143

```html
<!DOCTYPE html>
<html lang="en">
<head>
<meta charset="utf-8">
<title>KTR Associates Business Card</title>
<link href="https://fonts.googleapis.com/css2?family=Open+Sans:wght@300;400&display=swap" rel="stylesheet">
<style>
  :root {
    --page-bg: #d9d9d9;
    --card-white: #ffffff;
    --card-black: #0b0b0b;
    --card-black-glow: #2a2a2a;
    --ink: #1c1c1c;
    --green: #3f8f3a;
    --green-light: #6fae3c;
    --white: #ffffff;
  }
  * { margin: 0; padding: 0; box-sizing: border-box; }
  html, body {
    width: 1200px;
    height: 985px;
    overflow: hidden;
    background: var(--page-bg);
    font-family: "Open Sans", Arial, sans-serif;
  }
  .canvas {
    position: relative;
    width: 1200px;
    height: 985px;
  }
  .card {
    position: absolute;
    left: 320px;
    width: 560px;
    height: 320px;
    border-radius: 22px;
    overflow: hidden;
    box-shadow: 0 10px 28px rgba(0,0,0,0.22);
  }
  /* back side */
  .card-back {
    top: 110px;
    background: radial-gradient(ellipse at 50% 50%, var(--card-black-glow) 0%, var(--card-black) 70%);
    display: flex;
    align-items: center;
    justify-content: center;
  }
  .card-back .brand-name {
    color: var(--white);
    font-weight: 300;
    font-size: 40px;
    letter-spacing: 2px;
  }
  /* front side */
  .card-front {
    top: 510px;
    background: var(--card-white);
  }
  .front-brand {
    position: absolute;
    left: 40px;
    top: 62px;
    color: var(--ink);
    font-weight: 300;
    font-size: 40px;
    letter-spacing: 2px;
  }
  .front-band {
    position: absolute;
    left: 0;
    right: 0;
    top: 150px;
    height: 52px;
    background: var(--card-black);
  }
  .name-block {
    position: absolute;
    left: 300px;
    top: 154px;
    color: var(--white);
  }
  .person-name {
    font-weight: 400;
    font-size: 24px;
    line-height: 1.1;
  }
  .person-name .surname { color: var(--green); }
  .person-title {
    font-size: 13px;
    line-height: 1.2;
  }
  .contact-list {
    position: absolute;
    left: 300px;
    top: 220px;
    list-style: none;
    color: var(--ink);
    font-size: 16px;
    letter-spacing: 0.5px;
  }
  .contact-list li {
    display: flex;
    align-items: center;
    gap: 8px;
    margin-bottom: 8px;
  }
  .contact-icon {
    width: 18px;
    height: 18px;
    flex: none;
  }
  .bottom-band {
    position: absolute;
    left: 0;
    right: 0;
    bottom: 0;
    height: 26px;
    background: var(--card-black);
  }
</style>
</head>
<body>
<main class="canvas">
  <section class="card card-back" aria-label="Card back">
    <span class="brand-name">KTR Associates</span>
  </section>

  <section class="card card-front" aria-label="Card front">
    <span class="front-brand">KTR Associates</span>
    <div class="front-band"></div>
    <div class="name-block">
      <p class="person-name">Marta <span class="surname">Holloway</span></p>
      <p class="person-title">President</p>
    </div>
    <ul class="contact-list">
      <li>
        <svg class="contact-icon" viewBox="0 0 18 18" aria-hidden="true">
          <rect width="18" height="18" rx="4" fill="#3f8f3a"/>
          <path d="M6 4.5 L8 6.8 L7 8 Q8 10.5 10 11 L11.2 10 L13.5 12 L12.4 13.5 Q7.5 13.5 4.5 6 Z" fill="#ffffff"/>
        </svg>
        <span>919-555-0143</span>
      </li>
      <li>
        <svg class="contact-icon" viewBox="0 0 18 18" aria-hidden="true">
          <rect width="18" height="18" rx="4" fill="#3f8f3a"/>
          <text x="9" y="13" font-size="12" text-anchor="middle" fill="#ffffff" font-family="Open Sans, sans-serif">@</text>
        </svg>
        <span>marta@ktr-associates-mail.com</span>
      </li>
    </ul>
    <div class="bottom-band"></div>
  </section>
</main>
</body>
</html>
```